Yoga class opening. Little schedule for JUNE JULY and AUGUST

Flyer to promote an opening yoga class. The color of the docx haven't to be respected.

We want something joyfull, professional, clean and serious.

About the logo we oppened a contest at the same time so at the moment there is no logo but the logo color will be simple.

The phone number will change so you can poste a random one for the design that i can change by myself.

i recieved many creation in both side BUT i want something in 1 side :)

Target Market(s)

Yoga student. all age

Industry/Entity Type

It Professional

Logo Text

Yoga fern

Font styles to use
Sans Serif

Requirements
Must have
• The text present on the docx
Nice to have
• Some symbols about yoga ( Namasté signs, mandala, ... )
Should not have
• Not too much details it has to be clear.

```html
<!DOCTYPE html>
<html lang="fr">
<head>
<meta charset="utf-8">
<title>Yoga fern – Ouverture</title>
<link href="https://fonts.googleapis.com/css2?family=Tinos:wght@400;700&display=swap" rel="stylesheet">
<style>
  :root {
    --sun: #f6c12d;
    --ink: #161616;
    --paper: #ffffff;
    --band-text: #1b1b1b;
    --photo-light: #fbf4ee;
    --photo-warm: #f08a4b;
  }
  * { margin: 0; padding: 0; box-sizing: border-box; }
  html, body { width: 900px; height: 1200px; overflow: hidden; background: var(--paper); }
  body { font-family: "Tinos", "Times New Roman", serif; color: var(--ink); }
  .flyer { position: relative; width: 900px; height: 1200px; background: var(--paper); }
  .abs { position: absolute; white-space: nowrap; }

  .headline { left: 0; width: 900px; top: 38px; text-align: center; font-size: 56px; font-weight: 700; color: var(--sun); letter-spacing: 0.5px; }
  .subline { left: 0; width: 900px; top: 100px; text-align: center; font-size: 42px; font-weight: 400; letter-spacing: 0.3px; }
  .opening-band { left: 61px; top: 163px; width: 779px; height: 38px; background: var(--sun); color: var(--band-text); font-size: 18.5px; font-weight: 700; display: flex; align-items: center; justify-content: center; }
  .intro { left: 0; width: 900px; top: 216px; text-align: center; font-size: 16.5px; }

  .photo { left: 28px; top: 253px; width: 436px; height: 808px; }

  .farewell { left: 50px; top: 1090px; font-size: 36px; font-weight: 700; }

  .month { left: 477px; height: 31px; border-radius: 16px; background: var(--sun); color: var(--paper); font-size: 26px; font-weight: 700; padding-left: 8px; line-height: 31px; }
  .course-bar { left: 477px; height: 21px; background: var(--ink); color: var(--paper); font-size: 13.5px; font-weight: 700; padding-left: 7px; line-height: 21px; }
  .slot { left: 477px; font-size: 11.5px; line-height: 14px; }
  .slot .date { color: var(--sun); font-weight: 700; }
  .slot .time { position: absolute; top: 0; }

  .launch-box { left: 475px; top: 1024px; width: 359px; height: 76px; border: 2px dotted var(--ink); border-radius: 12px; text-align: center; }
  .launch-label { display: block; margin-top: 8px; font-size: 15px; font-weight: 700; letter-spacing: 0.4px; }
  .launch-date { display: block; margin-top: 2px; font-size: 35px; font-weight: 700; }

  .contact { left: 477px; font-size: 19px; font-weight: 700; }
  .contact .handle { color: var(--sun); }
</style>
</head>
<body>
<main class="flyer">
  <h1 class="abs headline">YOGA FERN NOUVEAU !!</h1>
  <h2 class="abs subline">VOTRE STUDIO DE YOGA A IXELLES</h2>
  <div class="abs opening-band">OUVERTURE LE 6 JUIN 2016 AU 212 RUE DES TILLEULS 1050 IXELLES</div>
  <p class="abs intro">En attendant le planning des cours de la rentrée, YOGA FERN vous propose ses stages et ateliers d’été.</p>

  <svg class="abs photo" viewBox="0 0 436 808" role="img" aria-label="Photo d'une femme en tenue orange assise en tailleur, mains jointes au-dessus de la tête">
    <defs>
      <radialGradient id="figureGlow" cx="50%" cy="62%" r="55%">
        <stop offset="0%" stop-color="var(--photo-warm)" stop-opacity="0.85"/>
        <stop offset="60%" stop-color="var(--photo-warm)" stop-opacity="0.3"/>
        <stop offset="100%" stop-color="var(--photo-light)" stop-opacity="0"/>
      </radialGradient>
    </defs>
    <rect width="436" height="808" fill="var(--paper)"/>
    <rect width="436" height="808" fill="url(#figureGlow)"/>
  </svg>

  <p class="abs farewell">UN BEL ETE A TOUS !</p>

  <!-- Juin -->
  <div class="abs month" style="top:275px;width:149px">JUIN</div>
  <div class="abs course-bar" style="top:325px;width:285px">Internship discovery YOGA 10:00 € 85 :</div>
  <p class="abs slot" style="top:358px"><span class="date">Du lundi 6 au vendredi 10 juin :</span><span class="time" style="left:189px">10h00 à 12h00 ou 18h00 à 20h00</span></p>
  <p class="abs slot" style="top:375px"><span class="date">Du lundi 13 au vendredi 17 juin :</span><span class="time" style="left:189px">10h00 à 12h00 ou 18h00 à 20h00</span></p>
  <p class="abs slot" style="top:391px"><span class="date">Du lundi 20 au vendredi 24 juin :</span><span class="time" style="left:189px">10h00 à 12h00 ou 18h00 à 20h00</span></p>
  <p class="abs slot" style="top:408px"><span class="date">Du lundi 27 au vendredi 1er juillet :</span><span class="time" style="left:189px">10h00 à 12h00 ou 18h00 à 20h00</span></p>

  <div class="abs course-bar" style="top:438px;width:353px">Atelier gestion du stress yoga/sophrologie 2h00 28 €</div>
  <p class="abs slot" style="top:468px"><span class="date">Samedi 11 juin</span><span class="time" style="left:114px">10h30 à 12h30</span></p>
  <p class="abs slot" style="top:486px"><span class="date">Samedi 11 juin</span><span class="time" style="left:114px">15h à 17h00</span></p>
  <p class="abs slot" style="top:502px"><span class="date">Dimanche 12 juin</span><span class="time" style="left:114px">10h30 à 12h30</span></p>
  <p class="abs slot" style="top:520px"><span class="date">Dimanche 12 juin</span><span class="time" style="left:114px">14h à 16h00</span></p>

  <!-- Juillet -->
  <div class="abs month" style="top:560px;width:186px">JUILLET</div>
  <div class="abs course-bar" style="top:611px;width:303px">Stage initiation à l’ASHTANGA 10h00 85 €</div>
  <p class="abs slot" style="top:645px"><span class="date">Du lundi 4 au vendredi 8 juillet :</span><span class="time" style="left:195px">10h00 à 12h00 ou 18h00 à 20h00</span></p>
  <p class="abs slot" style="top:662px"><span class="date">Du lundi 11 au vendredi 15 juillet :</span><span class="time" style="left:195px">10h00 à 12h00 ou 18h00 à 20h00</span></p>
  <p class="abs slot" style="top:678px"><span class="date">Du lundi 18 au vendredi 22 juillet :</span><span class="time" style="left:195px">10h00 à 12h00 ou 18h00 à 20h00</span></p>
  <p class="abs slot" style="top:696px"><span class="date">Du lundi 25 au vendredi 29 juillet :</span><span class="time" style="left:195px">10h00 à 12h00 ou 18h00 à 20h00</span></p>

  <div class="abs course-bar" style="top:725px;width:353px">Atelier gestion du stress yoga/sophrologie 2h00 28 €</div>
  <p class="abs slot" style="top:757px"><span class="date">Samedi 9 juillet</span><span class="time" style="left:141px">10h30 à 12h30</span></p>
  <p class="abs slot" style="top:774px"><span class="date">Samedi 9 juillet</span><span class="time" style="left:141px">15h00 à 17h00</span></p>
  <p class="abs slot" style="top:790px"><span class="date">Dimanche 10 juillet</span><span class="time" style="left:141px">10h30 à 12h30</span></p>
  <p class="abs slot" style="top:808px"><span class="date">Dimanche 10 juillet</span><span class="time" style="left:141px">14h00 à 16h00</span></p>

  <!-- Août -->
  <div class="abs month" style="top:850px;width:149px">AOUT</div>
  <div class="abs course-bar" style="top:898px;width:285px">Stage découverte du YOGA 10h00 85 €</div>
  <p class="abs slot" style="top:930px"><span class="date">Du lundi 1er au vendredi 5 août :</span><span class="time" style="left:189px">10h00 à 12h00 ou 18h00 à 20h00</span></p>
  <p class="abs slot" style="top:948px"><span class="date">Du lundi 8 au vendredi 12 août :</span><span class="time" style="left:189px">10h00 à 12h00 ou 18h00 à 20h00</span></p>
  <p class="abs slot" style="top:965px"><span class="date">Du lundi 15 au vendredi 19 août :</span><span class="time" style="left:189px">10h00 à 12h00 ou 18h00 à 20h00</span></p>
  <p class="abs slot" style="top:983px"><span class="date">Du lundi 22 au vendredi 26 août :</span><span class="time" style="left:189px">10h00 à 12h00 ou 18h00 à 20h00</span></p>

  <div class="abs launch-box">
    <span class="launch-label">DÉMARRAGE DU PLANNING ANNUEL LE</span>
    <span class="launch-date">5 SEPTEMBRE 2016</span>
  </div>

  <p class="abs contact" style="top:1126px">Plus d’info et inscription :</p>
  <p class="abs contact" style="top:1150px">Ou via notre page Sociabook : <span class="handle">yoga fern</span></p>
</main>
</body>
</html>
```